International Railway Company Needs a Brochure - KVR Steady & True for Railway

We need a brochure for an International Company based in Italy called 'KVR'. We develop innovative instruments used in Railway monitoring for diagnostic and maintenance. Our main product is Track Geometry Measurement System (TGMS) - TGMS measuring the track geometry is composed by two profile measurement instruments (left and right) and one inertial pack. All these instruments are installed on a single rigid rod, mounted on a bogie All our products are based on Laser Triangulation Method.
We appreciate to see designs that use color blue but is not required.
The final design should communicate financial safety and growth. Also The final design should communicate our motto 'Steady & True'.
We'll send you our Company Logo, photos and contents. We are open to any suggestions.

Our web site is http://www.kvrnovaro.it/home.html
Updates

We are launching the contest for KVR new logo. It will be finished in 2/5 days. Thanks for your work.

 

Target Market(s)

Our main customers are International Railway Companies (FTRV-France, KL-Germany, TPO-Italy, ZKH-Switzerland) but also private companies.
Please see our competitors brochure in file attached "PWT Track Measuring Systems_EN_v6.pdf"

Industry/Entity Type

Financial

Requirements
Must have
• The brochure must have 6 pages A4 format like the example file PWT Track Measuring Systems_EN_v6

Page 1: Cover Page - KVR Synthesis
Page 2: Synthesis of the following products with one image for each

TMS
TGMS
RPMS
TRMS
TVS
DV

Page 3: TGMS details
Page 4: TMS and RPMS details
Page 5: TRMS and TVS and DV details
Page 6: Contacts

The text is not important. We can add it in a second time.

The file 115643_2387209_226909_vector is Company Logo file.
The file Final_KVR source logo1-bw is "family" Product logo.

Please feel free to change color at both logo if you need to do it or make it trasparent.
Should not have
• In the final brochure we don't want to see our VAT/TVA/IVA

```html
<!DOCTYPE html>
<html lang="en">
<head>
<meta charset="utf-8">
<title>KVR Brochure – Back and Front Cover</title>
<link rel="stylesheet" href="https://fonts.googleapis.com/css2?family=Questrial&display=swap">
<style>
  :root {
    --stage: #d6d6d6;
    --stage-edge: #bdbdbd;
    --orange-light: #f0a27c;
    --orange: #d9663a;
    --orange-deep: #b8481f;
    --band-grey: #6e6e6e;
    --band-grey-dark: #4a4a4a;
    --white: #ffffff;
    --photo-light: #d9d9d9;
    --photo-mid: #7a7a7a;
    --photo-dark: #2b2b2b;
  }
  * { margin: 0; padding: 0; box-sizing: border-box; }
  html, body { width: 1200px; height: 1000px; overflow: hidden; }
  body {
    background: radial-gradient(ellipse at 50% 40%, var(--stage) 0%, var(--stage-edge) 100%);
    font-family: "Questrial", "Century Gothic", sans-serif;
    position: relative;
  }
  .page {
    position: absolute;
    top: 125px;
    width: 530px;
    height: 750px;
    overflow: hidden;
    box-shadow: 0 10px 30px rgba(0,0,0,0.25);
  }
  .back-cover { left: 60px; background: linear-gradient(160deg, var(--orange-light) 0%, var(--orange) 45%, var(--orange-deep) 100%); }
  .front-cover { left: 610px; }

  .brand {
    position: absolute;
    text-align: center;
  }
  .brand-name {
    font-size: 44px;
    letter-spacing: 6px;
    color: var(--white);
    line-height: 1;
  }
  .brand-tagline {
    margin-top: 10px;
    font-size: 11px;
    letter-spacing: 4px;
    text-transform: uppercase;
  }
  .back-cover .brand { right: 40px; top: 470px; }
  .back-cover .brand-tagline { color: var(--white); }

  .contact-band {
    position: absolute;
    left: 0; right: 0;
    top: 560px;
    height: 100px;
    background: linear-gradient(90deg, var(--band-grey-dark) 0%, var(--band-grey) 100%);
    border-top: 6px solid var(--band-grey-dark);
  }
  .contact-details {
    position: absolute;
    right: 28px; top: 10px;
    font-size: 11px;
    font-style: normal;
    line-height: 1.45;
    color: var(--white);
    text-align: left;
  }
  .back-cover .web-address {
    position: absolute;
    right: 28px; top: 680px;
    font-size: 20px;
    color: var(--white);
    letter-spacing: 1px;
  }
  .web-address strong { font-weight: 400; color: var(--band-grey-dark); }

  .cover-photo {
    position: absolute; inset: 0;
    background:
      radial-gradient(ellipse at 60% 38%, rgba(255,255,255,0.75) 0%, rgba(255,255,255,0) 45%),
      linear-gradient(170deg, var(--photo-light) 0%, var(--photo-mid) 45%, var(--photo-dark) 100%);
  }
  .front-cover .brand { left: 230px; top: 230px; }
  .front-cover .brand-name { color: var(--white); }
  .front-cover .brand-tagline { color: var(--orange); }

  .web-tab {
    position: absolute;
    right: 0; bottom: 0;
    width: 330px; height: 52px;
    background: var(--orange);
    border-top-left-radius: 26px;
    display: flex; align-items: center; justify-content: center;
    font-size: 20px;
    letter-spacing: 1px;
    color: var(--white);
  }
  .web-tab strong { font-weight: 400; color: var(--white); }
</style>
</head>
<body>

  <section class="page back-cover" aria-label="Back cover">
    <div class="brand">
      <div class="brand-name">KVR</div>
      <div class="brand-tagline">Steady &amp; True</div>
    </div>
    <div class="contact-band">
      <address class="contact-details">
        KVR S.r.l. Headquarters Via Castelletto, 18<br>
        28100 Novaro - NO ITALY<br>
        Tel: +39 0321 5548207<br>
        Fax: +39 0321 5548208<br>
        Email: info@kvrnovaro.it
      </address>
    </div>
    <div class="web-address">www.<strong>kvr</strong>novaro.it</div>
  </section>

  <section class="page front-cover" aria-label="Front cover">
    <div class="cover-photo" role="img" aria-label="Black and white photograph of curving railway tracks and an elevated track bed"></div>
    <div class="brand">
      <div class="brand-name">KVR</div>
      <div class="brand-tagline">Steady &amp; True</div>
    </div>
    <div class="web-tab">www.<strong>kvr</strong>novaro.it</div>
  </section>

</body>
</html>
```